Creat new BusinessCard for Brightpath Advisory!

Hello Creativ Designer. I need a new Businesscard for our brand new Company "Brightpath Coaching". We do Consulting for a better Life & Work Situation. to create Fulfillment, Sense, Motivation and healthy Work Places in Company's. So we try to create a better World and help the employee to like what they do!
So we would like to have 2 Sites on the card. On the Back we want to put this words: "The sole meaning of life, is to serve humanity" (it can be vertical oder horizontal). In the front there is the Logo (Black or White) and Adress+ and Slogan.

Slogan on the front: -Make your Business & Life to a better place-

Name: Lukas Fenwald
Titel: Founder - Visionary - Trainer
Adress: Based in Switzerland

Tel: +41 (0) 71 483 27 15
Email: hello@brightpath-coaching.ch
Homepage: www.brightpath-coaching.ch

Thanks for your inspired Ideas and your help to make the world to a better place! IT has to be ready to print and normal Size.

Target Market(s)

insurance, Bank, Telecom, industry, IT, Medical

Contact Information for Business Card

Breite: 85 mm x Höhe: 55 mm

Colors

Designer to choose colors to be used in the design.

Requirements
Nice to have
• Thanks for your Ideas so far!
• Maybe you can try/play with the colors: Purple Code #652C8F and Grey #979797 from the Zorvik Logo purple and grey (but only a soft combination, not to much)

```html
<!DOCTYPE html>
<html lang="en">
<head>
<meta charset="utf-8">
<title>Brightpath Coaching – Business Card</title>
<link href="https://fonts.googleapis.com/css2?family=Montserrat:wght@600;700&family=Crimson+Pro:wght@400;500&display=swap" rel="stylesheet">
<style>
  :root {
    --backdrop: #333333;
    --card: #ffffff;
    --ink: #000000;
    --paper: #ffffff;
    --muted: #b5b5b5;
  }
  * { margin: 0; padding: 0; box-sizing: border-box; }
  html, body { width: 1200px; height: 980px; overflow: hidden; background: var(--backdrop); }
  .stage { position: relative; width: 1200px; height: 980px; }
  .card { position: absolute; left: 355px; width: 515px; height: 308px; background: var(--card); overflow: hidden; }
  .card--front { top: 169px; }
  .card--back { top: 539px; }
  .band { position: absolute; left: 0; width: 100%; background: var(--ink); }
  .front-band { top: 166px; height: 87px; }
  .front-foot { top: 281px; height: 27px; }
  .mark-front { position: absolute; left: 45px; top: 100px; width: 116px; height: 116px; }
  .mark-back { position: absolute; left: 200px; top: 57px; width: 116px; height: 116px; }
  .mark-label {
    position: absolute; width: 100%; top: 50%; transform: translateY(-50%);
    text-align: center; font-family: 'Montserrat', sans-serif; font-weight: 700;
    font-size: 13px; letter-spacing: 0.5px;
  }
  .mark-front .mark-label { color: var(--paper); }
  .mark-back .mark-label { color: var(--ink); }
  .person-name {
    position: absolute; left: 168px; top: 132px;
    font-family: 'Montserrat', sans-serif; font-weight: 700; font-size: 34px;
    line-height: 1; color: var(--ink); letter-spacing: -0.3px;
  }
  .person-title {
    position: absolute; left: 158px; top: 169px; width: 350px;
    display: flex; align-items: center; gap: 6px;
    font-family: 'Crimson Pro', serif; font-size: 17px; color: var(--muted); white-space: nowrap;
  }
  .person-title .rule { flex: 1; height: 1px; background: var(--muted); }
  .contact {
    position: absolute; font-family: 'Crimson Pro', serif; font-size: 12.5px;
    color: var(--paper); white-space: nowrap; letter-spacing: 0.3px;
  }
  .contact--tel { left: 157px; top: 201px; }
  .contact--mail { left: 308px; top: 201px; }
  .contact--web { left: 224px; top: 221px; }
  .slogan {
    position: absolute; left: 0; width: 100%; top: 257px; text-align: center;
    font-family: 'Crimson Pro', serif; font-size: 16px; color: var(--ink); letter-spacing: 0.4px;
  }
  .back-band { top: 180px; height: 70px; display: flex; align-items: center; justify-content: center; }
  .brand-name {
    font-family: 'Montserrat', sans-serif; font-weight: 600; font-size: 24px;
    color: var(--paper); letter-spacing: 1.5px;
  }
  .motto {
    position: absolute; left: 0; width: 100%; top: 252px; text-align: center;
    font-family: 'Crimson Pro', serif; font-size: 16.5px; color: var(--ink); letter-spacing: 0.3px;
  }
</style>
</head>
<body>
<div class="stage">
  <section class="card card--front">
    <div class="band front-band"></div>
    <div class="band front-foot"></div>
    <div class="mark-front">
      <svg width="116" height="116" viewBox="0 0 116 116" aria-hidden="true">
        <circle cx="58" cy="58" r="56" fill="#000" stroke="#fff" stroke-width="3"/>
      </svg>
      <span class="mark-label">Brightpath</span>
    </div>
    <h1 class="person-name">Lukas Fenwald</h1>
    <p class="person-title"><span class="rule"></span>Founder - Visionary - Trainer<span class="rule"></span></p>
    <p class="contact contact--tel">Tel: +41 (0) 71 483 27 15</p>
    <p class="contact contact--mail">Email: hello@brightpath-coaching.ch</p>
    <p class="contact contact--web">www.brightpath-coaching.ch</p>
    <p class="slogan">-Make your Business &amp; Life to a better place-</p>
  </section>

  <section class="card card--back">
    <div class="mark-back">
      <svg width="116" height="116" viewBox="0 0 116 116" aria-hidden="true">
        <circle cx="58" cy="58" r="53" fill="none" stroke="#000" stroke-width="5"/>
      </svg>
    </div>
    <div class="band back-band"><span class="brand-name">BRIGHTPATH COACHING</span></div>
    <p class="motto">The sole meaning of life, is to serve humanity</p>
  </section>
</div>
</body>
</html>
```